Property Developer Business card design

we need a business card design + printing for a new Property developer company based in melbourne.
We are a group of investors investing in a property developer business. We have more projects involved in residential property as opposed to commercial property but we are involved in both market. we also provide consulting services with overseas investors willing to invest in the australian property market.
Updates
I have uploaded the logo. I'm not very convince with the colors of my logo... any suggestion please?.
Thanks guys!
Target Market(s)
property investors or person willing to purchase investment property
Industry/Entity Type
Residential
Contact Information for Business Card
Harbourne Capital Australia Pty Ltd
Look and feel
Each slider illustrates characteristics of the customer's brand and the style your logo design should communicate.

```html
<!DOCTYPE html>
<html lang="en">
<head>
<meta charset="utf-8">
<title>Harbourne Capital Australia – Business Cards</title>
<link rel="stylesheet" href="https://fonts.googleapis.com/css2?family=Questrial&family=Tenor+Sans&display=swap">
<style>
  :root {
    --backdrop: #e8e5de;
    --card-light: #ffffff;
    --card-edge: #cfd0d1;
    --ink: #1d1d1d;
    --blue: #1aa3e0;
    --blue-deep: #0f6fb3;
    --red: #e0202a;
    --red-deep: #a8141c;
    --rule: #333333;
  }
  * { box-sizing: border-box; margin: 0; padding: 0; }
  html, body { width: 1200px; height: 1200px; overflow: hidden; }
  body {
    background: var(--backdrop);
    position: relative;
    font-family: "Questrial", "Century Gothic", sans-serif;
    color: var(--ink);
  }
  .card {
    position: absolute;
    width: 512px;
    height: 295px;
    overflow: hidden;
    background: radial-gradient(ellipse at 42% 30%, var(--card-light) 0%, #eeeeee 45%, var(--card-edge) 100%);
    box-shadow: 0 2px 6px rgba(0,0,0,0.18);
  }
  .card--bars { left: 36px; top: 245px; }
  .card--brand { left: 613px; top: 258px; }
  .card--towers { left: 37px; top: 598px; }
  .card--split { left: 587px; top: 598px; }

  .brand-band {
    position: absolute;
    left: 0; right: 0; bottom: 0;
    height: 19px;
    background: linear-gradient(100deg, var(--blue) 0%, #1592d2 47.5%, var(--red-deep) 48%, var(--red) 100%);
  }

  .holder-name {
    position: absolute;
    font-family: "Tenor Sans", "Copperplate", sans-serif;
    font-variant: small-caps;
    font-size: 17px;
    letter-spacing: 1.2px;
    line-height: 1;
  }
  .holder-title {
    position: absolute;
    font-family: "Tenor Sans", "Copperplate", sans-serif;
    font-variant: small-caps;
    font-size: 11px;
    letter-spacing: 1px;
    line-height: 1;
  }
  .contact-list {
    position: absolute;
    list-style: none;
    font-size: 10px;
    line-height: 17.5px;
  }
  .contact-list li { display: flex; }
  .contact-label {
    width: 17px;
    font-family: "Tenor Sans", sans-serif;
    font-size: 11px;
    font-weight: 700;
  }

  .card--bars .holder-name, .card--towers .holder-name { left: 19px; top: 45px; }
  .card--bars .holder-title, .card--towers .holder-title { left: 19px; top: 64px; }
  .card--bars .contact-list, .card--towers .contact-list { left: 19px; top: 188px; }

  .skyline-art {
    position: absolute;
    left: 340px; top: 96px;
    width: 162px; height: 180px;
    background: linear-gradient(180deg, rgba(42,168,230,0.35) 0%, rgba(15,111,179,0.75) 100%);
  }

  .company-name {
    position: absolute;
    font-family: "Questrial", "Century Gothic", sans-serif;
    color: var(--blue-deep);
    text-align: center;
    line-height: 1.15;
  }
  .card--brand .company-name {
    left: 0; right: 0; top: 136px;
    font-size: 26px;
  }
  .company-mark {
    display: inline-block;
    width: 10px; height: 10px;
    background: var(--red);
    margin-right: 8px;
    vertical-align: middle;
  }
  .card--towers .company-name {
    left: 296px; top: 82px;
    width: 96px;
    font-size: 10px;
  }
  .card--split .company-name {
    left: 20px; top: 120px;
    width: 200px;
    font-size: 20px;
  }

  .tower-art {
    position: absolute;
    left: 307px; top: 128px;
    width: 205px; height: 148px;
    background: linear-gradient(90deg, rgba(26,163,224,0.55) 0%, rgba(26,163,224,0.55) 40%, rgba(224,32,42,0.55) 60%, rgba(168,20,28,0.7) 100%);
  }

  .divider {
    position: absolute;
    left: 258px; top: 50px;
    width: 1px; height: 156px;
    background: var(--rule);
  }
  .card--split .holder-name { left: 266px; top: 56px; font-size: 15px; }
  .card--split .holder-title { left: 266px; top: 74px; font-size: 10px; }
  .card--split .contact-list { left: 266px; top: 143px; }
</style>
</head>
<body>

  <section class="card card--bars" aria-label="Business card front, skyline graphic">
    <p class="holder-name">Daniel Marsh</p>
    <p class="holder-title">Managing Director</p>
    <ul class="contact-list">
      <li><span class="contact-label">T</span>+61 3 9012 5580</li>
      <li><span class="contact-label">M</span>0400 182 345</li>
      <li><span class="contact-label">E</span>daniel.marsh@harbournecapital.com.au</li>
      <li><span class="contact-label">A</span>14 Wattle Grove Tarneit VIC 3029</li>
    </ul>
    <div class="skyline-art" role="img" aria-label="Illustration of blue city skyscrapers"></div>
    <div class="brand-band"></div>
  </section>

  <section class="card card--brand" aria-label="Business card back">
    <p class="company-name"><span class="company-mark"></span>Harbourne Capital<br>Australia</p>
    <div class="brand-band"></div>
  </section>

  <section class="card card--towers" aria-label="Business card front, tower graphic">
    <p class="holder-name">Daniel Marsh</p>
    <p class="holder-title">Managing Director</p>
    <ul class="contact-list">
      <li><span class="contact-label">T</span>+61 3 9012 5580</li>
      <li><span class="contact-label">M</span>0400 182 345</li>
      <li><span class="contact-label">E</span>daniel.marsh@harbournecapital.com.au</li>
      <li><span class="contact-label">A</span>14 Wattle Grove Tarneit VIC 3029</li>
    </ul>
    <div class="tower-art" role="img" aria-label="Illustration of two striped apartment towers, one blue and one red"></div>
    <p class="company-name">Harbourne Capital Australia</p>
    <div class="brand-band"></div>
  </section>

  <section class="card card--split" aria-label="Business card, single-sided layout">
    <p class="company-name">Harbourne Capital<br>Australia</p>
    <div class="divider"></div>
    <p class="holder-name">Daniel Marsh</p>
    <p class="holder-title">Managing Director</p>
    <ul class="contact-list">
      <li><span class="contact-label">T</span>+61 3 9012 5580</li>
      <li><span class="contact-label">M</span>0400 182 345</li>
      <li><span class="contact-label">E</span>daniel.marsh@harbournecapital.com.au</li>
      <li><span class="contact-label">A</span>14 Wattle Grove Tarneit VIC 3029</li>
    </ul>
    <div class="brand-band"></div>
  </section>

</body>
</html>
```